Velitor creating new logo and business card design

Velitor is a consulting and business contribution for professional digital and real estate. We are specializing in lead generation / prospect want to invest in real estate that we connect with wealth manager or promoters. We identify prospects on all France, we call them and we put them in touch with professional able to meet their need. We wish to highlight our logo through the creation of value we bring to our customers. We provide them with contacts we obtained with tact, hence the solgan: tact in contact ... The logo should be created with the name Velitor. Playing with the name. If possible, put the slogan with the name and logo

Target Market(s)

Digital Immobiler

Industry/Entity Type

Digital

Contact Information for Business Card

RECTO :
Carvel Tiruan
CEO/Fondateur
Tel : 06 52 19 83 07
mail : tiruan.carvel@postelia.fr
VELITOR
14 rue des Orpailleurs
92340 Brevanne
VERSO : juste le logo

Logo Text

Velitor, le flair du lien

Font styles to use
Sans Serif
Decorative

Colors
ec1f27
e34297
85cae6
fbed22
f37122
9bcb3b
6b449b

Requirements
Must have
• We wish to have a logo that reflects our position as an innovative company and digital. The logo must be fluid, colorful and futuristic. We wish to highlight our logo through the creation of value we bring to our customers. We bring the contacts we have achieved tactfully, hence the solgan: tact in contact ...
Nice to have
• We like the Pluvex logo, toravine ... can bring out effect with a profile or target such I leave you free rein to your immagination
Should not have
• Nothing to report

```html
<!DOCTYPE html>
<html lang="fr">
<head>
<meta charset="utf-8">
<title>Velitor – cartes de visite</title>
<link rel="stylesheet" href="https://fonts.googleapis.com/css2?family=Yellowtail&family=Quicksand:wght@500;600&display=swap">
<style>
  :root {
    --bg: #e9e9ea;
    --paper: #ffffff;
    --ink: #2a2a2c;
    --slate: #2e2e31;
    --red: #ec1f27;
    --orange: #f37122;
    --green: #9bcb3b;
    --teal: #2a8c98;
    --text-light: #f2f2f2;
  }
  * { box-sizing: border-box; margin: 0; padding: 0; }
  html, body { width: 1200px; height: 848px; overflow: hidden; }
  body {
    background: var(--bg);
    display: flex;
    align-items: center;
    justify-content: center;
    gap: 44px;
    font-family: "Quicksand", "Century Gothic", sans-serif;
  }
  .card {
    width: 530px;
    height: 303px;
    background: var(--paper);
    position: relative;
    overflow: hidden;
    box-shadow: 0 6px 18px rgba(0,0,0,.18);
  }

  /* brand lockup */
  .brand { display: flex; align-items: center; gap: 14px; }
  .brand__mark {
    width: 46px; height: 38px;
    border-radius: 6px;
    background: var(--teal);
  }
  .brand__name {
    font-family: "Yellowtail", cursive;
    font-size: 58px;
    color: var(--ink);
    line-height: 1;
  }

  /* recto */
  .recto { display: flex; }
  .recto__brand-side {
    width: 52%;
    display: flex;
    align-items: center;
    justify-content: center;
  }
  .recto__brand-side .brand { flex-direction: row-reverse; }
  .recto__divider { width: 9px; display: flex; flex-direction: column; }
  .recto__divider span { flex: 1; }
  .recto__info {
    flex: 1;
    background: var(--slate);
    color: var(--text-light);
    padding: 34px 0 0 26px;
  }
  .holder__name {
    font-family: "Yellowtail", cursive;
    font-size: 34px;
    line-height: 1;
    color: #fff;
  }
  .holder__role {
    font-size: 17px;
    font-weight: 600;
    color: var(--red);
    margin: 4px 0 22px;
  }
  .holder__role .accent { color: var(--orange); }
  .contact { list-style: none; font-size: 12.5px; line-height: 1.55; }
  .contact li { display: flex; align-items: center; gap: 7px; }
  .contact li.plain { padding-left: 19px; }
  .contact svg { width: 12px; height: 12px; flex: none; }

  /* verso */
  .verso { display: flex; align-items: center; justify-content: center; }
  .edge {
    position: absolute; left: 0; right: 0; height: 26px;
    display: flex; flex-direction: column;
  }
  .edge--top { top: 0; }
  .edge--bottom { bottom: 0; flex-direction: column-reverse; }
  .edge__band { height: 17px; background: var(--slate); }
  .edge__stripe { height: 9px; display: flex; }
  .edge__stripe span { flex: 1; }
  .verso .brand__name { font-size: 66px; }
  .verso .brand__mark { width: 52px; height: 42px; }

  .c-red { background: var(--red); }
  .c-orange { background: var(--orange); }
  .c-green { background: var(--green); }
  .c-teal { background: var(--teal); }
</style>
</head>
<body>

  <article class="card recto" aria-label="Carte de visite, recto">
    <div class="recto__brand-side">
      <div class="brand">
        <span class="brand__mark" aria-hidden="true"></span>
        <span class="brand__name">Velitor</span>
      </div>
    </div>
    <div class="recto__divider" aria-hidden="true">
      <span class="c-teal"></span><span class="c-green"></span><span class="c-orange"></span><span class="c-red"></span>
    </div>
    <div class="recto__info">
      <p class="holder__name">Carvel Tiruan</p>
      <p class="holder__role">CEO <span class="accent">/ Fondateur</span></p>
      <ul class="contact">
        <li>
          <svg viewBox="0 0 12 12" aria-hidden="true"><circle cx="6" cy="6" r="6" fill="#ec1f27"/><path d="M4 3.2c.3-.3.7-.3.9 0l.5.8c.2.3.1.6-.1.8l-.3.3c.3.6.8 1.1 1.4 1.4l.3-.3c.2-.2.5-.3.8-.1l.8.5c.3.2.3.6 0 .9l-.4.4c-2 .3-4.5-2.2-4.3-4.3z" fill="#fff"/></svg>
          06 52 19 83 07
        </li>
        <li>
          <svg viewBox="0 0 12 12" aria-hidden="true"><circle cx="6" cy="6" r="6" fill="#9bcb3b"/><rect x="3" y="4" width="6" height="4.2" rx=".5" fill="none" stroke="#fff" stroke-width=".9"/><path d="M3.2 4.3 6 6.4l2.8-2.1" fill="none" stroke="#fff" stroke-width=".9"/></svg>
          tiruan.carvel@postelia.fr
        </li>
        <li>
          <svg viewBox="0 0 12 12" aria-hidden="true"><circle cx="6" cy="6" r="6" fill="#2a8c98"/><path d="M3 6.2 6 3.4l3 2.8M4 5.6V8.6h4V5.6" fill="none" stroke="#fff" stroke-width=".9"/></svg>
          VELITOR
        </li>
        <li class="plain">14 rue des Orpailleurs</li>
        <li class="plain">92340 Brevanne</li>
      </ul>
    </div>
  </article>

  <article class="card verso" aria-label="Carte de visite, verso">
    <div class="edge edge--top" aria-hidden="true">
      <div class="edge__band"></div>
      <div class="edge__stripe"><span class="c-teal"></span><span class="c-green"></span><span class="c-orange"></span><span class="c-red"></span></div>
    </div>
    <div class="brand">
      <span class="brand__mark" aria-hidden="true"></span>
      <span class="brand__name">Velitor</span>
    </div>
    <div class="edge edge--bottom" aria-hidden="true">
      <div class="edge__band"></div>
      <div class="edge__stripe"><span class="c-red"></span><span class="c-orange"></span><span class="c-green"></span><span class="c-teal"></span></div>
    </div>
  </article>

</body>
</html>
```